Looking for awesome business card design with attached existing logo

We are a water, mold, and fire damage restoration company called "Torvane Seco" Looking for an awesome business card that is edgy yet professional and unique. Show me what you got!

```html
<!DOCTYPE html>
<html lang="en">
<head>
<meta charset="utf-8">
<title>Torvane Seco – Business Card</title>
<link rel="stylesheet" href="https://fonts.googleapis.com/css2?family=Montserrat:wght@400;500;700&display=swap">
<style>
  :root {
    --backdrop: #cbcbcb;
    --card-teal: #2c4856;
    --pattern-teal: #2a4653;
    --gold: #dc9a2a;
    --muted-gold: #8c7638;
    --red: #c4202f;
    --white: #ffffff;
    --soft-white: #e9eef0;
  }
  * { box-sizing: border-box; margin: 0; padding: 0; }
  html, body { width: 1200px; height: 788px; overflow: hidden; }
  body {
    background: var(--backdrop);
    font-family: "Montserrat", sans-serif;
    position: relative;
  }
  .card {
    position: absolute;
    top: 234px;
    width: 560px;
    height: 320px;
    background: var(--card-teal);
    overflow: hidden;
    box-shadow: 0 10px 24px rgba(0,0,0,0.25);
  }
  .card--front { left: 20px; }
  .card--back { left: 620px; }

  /* Front */
  .edge-stripe {
    position: absolute; left: 0; bottom: 0; height: 7px; width: 100%;
    display: flex;
  }
  .edge-stripe__gold { flex: 0 0 290px; background: var(--gold); }
  .edge-stripe__red { flex: 1; background: var(--red); }
  .corner-tab {
    position: absolute; right: 0; top: 22px; width: 26px; height: 24px;
    background: var(--gold);
  }
  .person {
    position: absolute; right: 40px; top: 26px; text-align: right;
  }
  .person__name {
    color: var(--gold); font-weight: 700; font-size: 22px; letter-spacing: 1.5px;
    text-transform: uppercase; line-height: 1.1;
  }
  .person__title {
    color: var(--white); font-size: 12px; font-weight: 400; margin-top: 3px;
  }
  .mark-ring {
    position: absolute; right: 62px; top: 100px; width: 128px; height: 128px;
    border: 10px solid var(--muted-gold); border-radius: 50%;
  }
  .brand {
    position: absolute; left: 38px; top: 130px;
    display: flex; align-items: center; gap: 10px;
  }
  .brand__dot {
    width: 16px; height: 16px; border-radius: 50%; background: var(--gold);
  }
  .brand__name {
    color: var(--white); font-weight: 700; font-size: 28px; letter-spacing: 1px;
    text-transform: uppercase;
  }
  .contact {
    position: absolute; left: 40px; top: 186px; color: var(--white);
    font-size: 12px; line-height: 16px;
  }
  .contact__address { margin-bottom: 10px; }
  .contact__list { list-style: none; }
  .contact__item { display: flex; align-items: center; gap: 7px; }
  .contact__icon { width: 10px; height: 10px; flex: 0 0 10px; }

  /* Back */
  .back-pattern {
    position: absolute; inset: 0;
    background: linear-gradient(160deg, #3a5a68 0%, var(--pattern-teal) 55%, #233c48 100%);
  }
  .back-brand {
    position: absolute; left: 50%; top: 50%; transform: translate(-50%, -50%);
    display: flex; align-items: center; gap: 8px;
  }
  .back-brand__dot { width: 12px; height: 12px; border-radius: 50%; background: var(--gold); }
  .back-brand__name {
    color: var(--gold); font-weight: 700; font-size: 18px; letter-spacing: 1px;
    text-transform: uppercase;
  }
</style>
</head>
<body>
  <section class="card card--front">
    <div class="corner-tab"></div>
    <div class="person">
      <p class="person__name">Dale Fenwick</p>
      <p class="person__title">CEO/Founder</p>
    </div>
    <div class="mark-ring"></div>
    <div class="brand">
      <span class="brand__dot"></span>
      <span class="brand__name">Torvane Seco</span>
    </div>
    <div class="contact">
      <p class="contact__address">Unit 4- 88 Harbour Road<br>Lakeview, BC</p>
      <ul class="contact__list">
        <li class="contact__item">
          <svg class="contact__icon" viewBox="0 0 10 10"><path d="M2 1 L4 1 L4.6 3 L3.4 4 Q4.6 6 6 6.6 L7 5.4 L9 6 L9 8 Q5 9 1 2 Z" fill="#dc9a2a"/></svg>
          555-014-2386
        </li>
        <li class="contact__item">
          <svg class="contact__icon" viewBox="0 0 10 10"><rect x="2.5" y="0.5" width="5" height="9" rx="1" fill="none" stroke="#dc9a2a" stroke-width="1.2"/></svg>
          555-017-9041
        </li>
        <li class="contact__item">
          <svg class="contact__icon" viewBox="0 0 10 10"><rect x="0.5" y="2" width="9" height="6.5" fill="#dc9a2a"/><path d="M0.5 2 L5 5.5 L9.5 2" fill="none" stroke="#2c4856" stroke-width="1"/></svg>
          info@torvaneseco.com
        </li>
        <li class="contact__item">
          <svg class="contact__icon" viewBox="0 0 10 10"><circle cx="5" cy="5" r="4.5" fill="#dc9a2a"/><path d="M0.5 5 H9.5 M5 0.5 V9.5" stroke="#2c4856" stroke-width="0.8"/></svg>
          www.torvaneseco.com
        </li>
      </ul>
    </div>
    <div class="edge-stripe">
      <span class="edge-stripe__gold"></span>
      <span class="edge-stripe__red"></span>
    </div>
  </section>

  <section class="card card--back">
    <div class="back-pattern" role="img" aria-label="Repeating pattern of the company mark in tonal teal"></div>
    <div class="back-brand">
      <span class="back-brand__dot"></span>
      <span class="back-brand__name">Torvane Seco</span>
    </div>
  </section>
</body>
</html>
```